Kestrel Plumbing business card full re design & logo design

Kestrel Plumbing is a Sydney based mechanical plumbing contractor company.
We would like a full redesign with new logo etc which we can take to a future website, uniforms, vehicle sign writing etc.
Blue is my preferred choice of colour but i would be open to see a couple of alternatives thrown in the mix to see how they compare. I am open to see on white cards, black cards etc. Open to many new ideas.
Please see attached original business cards which have been used for the last 5 years.

Target Market(s)

Mechanical services industry.

Industry/Entity Type

Plumbing

Contact Information for Business Card

Dale Fenmore
Director

Mob: 0427 596 418
Email: dale@kestrelplumbing-demo.net.au
PO BOX 782
Brenfield NSW 2164
Lic: 518604k

Logo Text

Kestrel Plumbing

Font styles to use
Sans Serif

Colors
0655a3
3276b5
0792cd
33a6d7
85cae6
000000
333333
474747

Requirements
Must have
• Things that make it very professional and very well presented.
Nice to have
• Same description or very similar to attached uploaded file
Should not have
• Anything that makes it look unprofessional or cartoony.

```html
<!DOCTYPE html>
<html lang="en">
<head>
<meta charset="utf-8">
<title>Kestrel Plumbing – Business Card</title>
<link href="https://fonts.googleapis.com/css2?family=Questrial&display=swap" rel="stylesheet">
<style>
  :root{
    --blue-deep:#0655a3;
    --blue:#3276b5;
    --blue-bright:#0792cd;
    --blue-light:#33a6d7;
    --blue-pale:#85cae6;
    --black:#000000;
    --charcoal:#333333;
    --graphite:#474747;
    --backdrop:#e4e5e7;
    --white:#ffffff;
  }
  *{box-sizing:border-box;margin:0;padding:0}
  html,body{width:1200px;height:900px;overflow:hidden}
  body{
    background:var(--backdrop);
    font-family:"Questrial",sans-serif;
    position:relative;
  }
  .card{
    position:absolute;
    top:285px;
    width:540px;height:330px;
    border-radius:22px;
    overflow:hidden;
    background:radial-gradient(ellipse at 60% 40%, #2a2a2a 0%, #111 55%, var(--black) 100%);
    box-shadow:0 18px 30px rgba(0,0,0,.28);
  }
  .card--front{left:40px}
  .card--back{left:620px}

  .front-shape{position:absolute;inset:0}

  .logo-art{
    position:absolute;
    border-radius:10px;
    background:linear-gradient(160deg,#5a5a5a 0%,#2d2d2d 40%,var(--blue-deep) 100%);
  }
  .card--front .logo-art{left:40px;top:40px;width:170px;height:160px}
  .card--back .logo-art{left:210px;top:40px;width:120px;height:120px;background:linear-gradient(160deg,#d8d8d8 0%,#9a9a9a 45%,var(--blue-deep) 100%)}

  .wordmark{
    position:absolute;
    font-size:30px;
    line-height:1;
    letter-spacing:.5px;
    white-space:nowrap;
  }
  .card--front .wordmark{left:22px;top:220px;color:var(--charcoal);font-size:27px}
  .card--back .wordmark{left:0;right:0;top:170px;text-align:center;color:var(--white)}

  .contact{
    position:absolute;left:292px;top:58px;
    color:var(--white);font-size:12.5px;
    white-space:nowrap;
  }
  .contact__name{color:var(--blue-light);font-size:19px;letter-spacing:.3px}
  .contact__role{font-size:12.5px;margin-top:4px;color:#e6e6e6}
  .contact__list{list-style:none;margin-top:40px}
  .contact__item{display:flex;align-items:flex-start;gap:8px;line-height:19px}
  .contact__item + .contact__item{margin-top:6px}
  .contact__item--tight{margin-top:1px !important}
  .contact__icon{width:14px;height:14px;flex:none;margin-top:2px;fill:var(--blue-bright)}
  .contact__licence{margin-top:18px;padding-left:22px}
  .contact__label{color:var(--blue-light)}

  .speciality-title{
    position:absolute;left:0;right:0;top:222px;
    text-align:center;
    color:var(--blue-bright);
    font-size:12px;letter-spacing:1.5px;
  }
  .speciality-title span{border-bottom:1px solid var(--blue-bright);padding-bottom:2px}
  .services{
    position:absolute;left:0;right:0;top:248px;
    display:flex;justify-content:space-between;
    padding:0 34px;
    list-style:none;
    font-size:12.5px;letter-spacing:1.4px;text-transform:uppercase;
  }
  .services__col{display:flex;flex-direction:column;gap:8px;text-align:center}
  .services__col:nth-child(1){margin-top:14px}
  .services__col:nth-child(3){margin-top:-8px}
  .service--blue{color:var(--blue-bright)}
  .service--white{color:var(--white)}
</style>
</head>
<body>

<section class="card card--front" aria-label="Business card front">
  <svg class="front-shape" viewBox="0 0 540 330" width="540" height="330" aria-hidden="true">
    <path d="M0 0 H255 Q285 175 195 330 H0 Z" fill="var(--white)"/>
    <path d="M255 0 H282 Q304 170 195 330 Q285 175 255 0 Z" fill="var(--blue-deep)"/>
    <path d="M268 0 H274 Q294 170 195 330 Q285 175 268 0 Z" fill="var(--blue-light)" opacity=".6"/>
  </svg>
  <div class="logo-art" role="img" aria-label="Logo illustration: plumber with wrench in front of pipework"></div>
  <div class="wordmark">Kestrel Plumbing</div>

  <div class="contact">
    <div class="contact__name">Dale Fenmore</div>
    <div class="contact__role">Director</div>
    <ul class="contact__list">
      <li class="contact__item">
        <svg class="contact__icon" viewBox="0 0 24 24" aria-hidden="true"><path d="M6.6 10.8a15.2 15.2 0 0 0 6.6 6.6l2.2-2.2c.3-.3.7-.4 1-.2 1.1.4 2.3.6 3.6.6.6 0 1 .4 1 1V20c0 .6-.4 1-1 1A17 17 0 0 1 3 4c0-.6.4-1 1-1h3.5c.6 0 1 .4 1 1 0 1.3.2 2.5.6 3.6.1.3 0 .7-.2 1z"/></svg>
        <span>0427 596 418</span>
      </li>
      <li class="contact__item">
        <svg class="contact__icon" viewBox="0 0 24 24" aria-hidden="true"><path d="M12 3 2 12h3v8h5v-6h4v6h5v-8h3z"/></svg>
        <span>PO BOX 782<br>Brenfield NSW 2164</span>
      </li>
      <li class="contact__item">
        <svg class="contact__icon" viewBox="0 0 24 24" aria-hidden="true"><path d="M12 2a10 10 0 1 0 0 20 10 10 0 0 0 0-20zm6.9 6h-3a15 15 0 0 0-1.3-3.9A8 8 0 0 1 18.9 8zM12 4c.8 1.2 1.5 2.5 1.9 4h-3.8c.4-1.5 1.1-2.8 1.9-4zM4.3 14a8 8 0 0 1 0-4h3.4a16 16 0 0 0 0 4zm.8 2h3a15 15 0 0 0 1.3 3.9A8 8 0 0 1 5.1 16zm3-8h-3a8 8 0 0 1 4.3-3.9A15 15 0 0 0 8.1 8zM12 20c-.8-1.2-1.5-2.5-1.9-4h3.8c-.4 1.5-1.1 2.8-1.9 4zm2.3-6H9.7a14 14 0 0 1 0-4h4.6a14 14 0 0 1 0 4zm.3 5.9c.6-1.2 1-2.5 1.3-3.9h3a8 8 0 0 1-4.3 3.9zm1.7-5.9a16 16 0 0 0 0-4h3.4a8 8 0 0 1 0 4z"/></svg>
        <span>www.kestrelplumbing-demo.net.au</span>
      </li>
      <li class="contact__item contact__item--tight">
        <svg class="contact__icon" viewBox="0 0 24 24" aria-hidden="true"><path d="M3 5h18v14H3zm2 2v.5l7 4.5 7-4.5V7zm0 2.9V17h14V9.9l-7 4.5z"/></svg>
        <span>dale@kestrelplumbing-demo.net.au</span>
      </li>
    </ul>
    <div class="contact__licence"><span class="contact__label">Lic:</span> 518604k</div>
  </div>
</section>

<section class="card card--back" aria-label="Business card back">
  <div class="logo-art" role="img" aria-label="Logo illustration: plumber with wrench in front of pipework"></div>
  <div class="wordmark">Kestrel Plumbing</div>
  <div class="speciality-title"><span>SPECIALISING IN</span></div>
  <ul class="services">
    <li class="services__col">
      <span class="service--blue">Make Good</span>
      <span class="service--white">Plant Room Works</span>
    </li>
    <li class="services__col">
      <span class="service--white">Refubishment</span>
      <span class="service--blue">Shut Downs</span>
    </li>
    <li class="services__col">
      <span class="service--blue">Tenancy Fit Out</span>
      <span class="service--white">Change Overs</span>
    </li>
  </ul>
</section>

</body>
</html>
```